Packaging Design Required for Premium Skincare Range

We require design for packaging boxes and labels (label to be printed via silkscreen on the bottles) for our skincare products. The overall look should be streamlined for the entire range, so as to have a strong brand image.

As these products are made in Singapore, we would like to incorporate a bit of ‘batik’ element into the design of boxes. A tiny symbol of the ‘Lion Head’ should be placed next to the words ‘Made in Singapore’. Attached is a file of the ‘Lion Head’.

Look and feel:
Upmarket, premium, elegant, feminine, natural

Examples of designs we like:
www.velumira.com
https://www.quorin.com/sg/
http://bownecosmetics.com/bowne-shop-skincare

The above are 3 different design concepts. Please explore how to integrate elements of these 3 concepts to come up with something original. The final design should communicate high product efficacy, elegance, premium and natural.

Design Scope:
1. Packaging Boxes:
Colors can be used to differentiate one product from another. However, the brand name and icon should be the same color for all products. The final print ready artwork should be of the right size/proportion to contain the bottles.

2. Labels (To be printed via silkscreen on the bottles):
One single color only for each product label. The pantone color is stated in the information for each product in the attached file. The final print ready artwork should be of the right size/proportion to be printed on the bottles.

Product Range (Total 6 products):
1. Amino Acid Cleansing Mousse
(Height of printable area of bottle: 10.8cm
Height of whole bottle with cap: 17cm
Diameter: 4.7cm)

2. Revitalizing Tonic
(Height of printable area of bottle: 13.6cm
Height of whole bottle with cap: 17.5cm
Diameter: 4cm) (The actual cap for this bottle is white and
not brown in the photo)

3. Soothing Moisturizer with Antioxidants
(Height of printable area of bottle: 9cm
Height of whole bottle with cap: 16.3cm
Diameter: 2.8cm)

4. Pore Clarifying Essence
Diameter: 2.5cm)

5. Intense Whitening Serum
Diameter: 2.8cm)

6. Cell Repair Concentrate
Diameter: 2.8cm)

Attached are the various files:
1. Brand logo (pantone 2755)
2. Lion Head symbol (pantone 032)
3. Information for each product's packaging and label
4. Photos of bottles
5. Examples of batik motifs.
Please feel free to look for other batik motifs which you feel can achieve the design effect. Also, it's for the outer packaging boxes only, not for the silkscreen label. Please explore how to integrate into the design in a tasteful and elegant way, without overwhelming or clutter. Or if your design is better without the batik motifs, please feel free to suggest.

Artwork files should be:
- Print-ready editable ai, png, eps, jpg files
- Includes front, back, and sides of boxes and labels
- Include source files
- Include 3-D mock-ups

Women of all ages, beauty bloggers, people who cares about their skin and want to look good, skincare connoissuers

• Century New Gothic or similar

• A strong brand image, a brand that communicates class, product efficacy, & natural premium ingredients.
• Clutter, embossing

```html
<!DOCTYPE html>
<html lang="en">
<head>
<meta charset="utf-8">
<title>Lumavera Amino Acid Cleansing Mousse – Box Artwork</title>
<link href="https://fonts.googleapis.com/css2?family=Lato:wght@400;700&family=Oswald:wght@300&family=Playfair+Display:wght@400&display=swap" rel="stylesheet">
<style>
  :root {
    --page-bg: #eceef3;
    --box-white: #ffffff;
    --side-tint: #f6f6f8;
    --brand-navy: #3a3885;
    --accent-blue: #2aa6df;
    --ornament-light: #d7eefa;
    --ornament-mid: #a9dcf4;
    --title-ink: #2b2b33;
    --body-ink: #4a4a52;
    --claim-ink: #8c8c96;
  }
  * { margin: 0; padding: 0; box-sizing: border-box; }
  html, body { width: 1200px; height: 687px; overflow: hidden; }
  body {
    background: var(--page-bg);
    display: flex;
    align-items: center;
    justify-content: center;
  }
  .box-net {
    display: flex;
    height: 610px;
    box-shadow: 0 10px 30px rgba(60, 60, 90, 0.12);
  }
  .panel { position: relative; height: 100%; overflow: hidden; }

  /* Side panel: ingredients */
  .side-panel {
    width: 190px;
    background: var(--side-tint);
    border-right: 1px solid #e3e3ea;
    padding: 34px 18px 0 18px;
    text-align: right;
  }
  .ingredients-heading {
    font-family: "Playfair Display", serif;
    font-size: 12px;
    letter-spacing: 0.5px;
    color: var(--body-ink);
    text-decoration: underline;
    text-align: left;
    padding-left: 8px;
    margin-bottom: 14px;
  }
  .ingredients-list {
    font-family: "Lato", sans-serif;
    font-size: 11.5px;
    line-height: 16.5px;
    color: var(--body-ink);
  }

  /* Front panel */
  .front-panel {
    width: 280px;
    background: var(--box-white);
    padding-top: 44px;
  }
  .brand-lockup {
    display: flex;
    flex-direction: column;
    align-items: center;
    gap: 12px;
  }
  .brand-mark {
    width: 78px; height: 78px;
    border: 5px solid var(--brand-navy);
    border-radius: 50%;
  }
  .brand-name {
    font-family: "Lato", sans-serif;
    font-weight: 700;
    font-size: 25px;
    letter-spacing: 0.5px;
    color: var(--brand-navy);
  }
  .product-title {
    margin: 72px 0 0 18px;
    padding-left: 10px;
    border-left: 2px solid var(--accent-blue);
    font-family: "Playfair Display", serif;
    font-size: 28px;
    line-height: 38px;
    color: var(--title-ink);
  }
  .product-claims {
    list-style: none;
    margin: 58px 0 0 30px;
    font-family: "Oswald", sans-serif;
    font-weight: 300;
    font-size: 11px;
    line-height: 17px;
    color: var(--claim-ink);
    text-transform: uppercase;
  }
  .batik-band {
    position: absolute;
    left: 0; right: 0; bottom: 0;
    height: 170px;
    background: linear-gradient(180deg, rgba(255,255,255,0) 0%, var(--ornament-light) 45%, var(--ornament-mid) 100%);
  }
  .side-panel .batik-band { height: 200px; }
</style>
</head>
<body>
  <main class="box-net">
    <section class="panel side-panel">
      <h2 class="ingredients-heading">INGREDIENTS</h2>
      <p class="ingredients-list">Distilled water, Sodium Cocoyl Glutamate, Potassium Cocoyl Glycinate, Polyglceryl-4 Laurate/Sebacate, Polyglyceryl-4 Caprylate/Caprate, Sodium PEG-7 Olive Oil Carboxylate, Olive Oil PEG-7 Esters, Sodium PCA, Sorbitol, Serine, Glycine, Glutamic Acid, lanine, Lysine, Arginine, Threonine, Proline, Citrus Sinesis (Sweet Orange) Essential Oil, Lavendula Dentata (Lavender) Essential Oil, Phenoxyethanol, DMDM Hydantoin, Iodopropynyl Butylcarbamate</p>
      <div class="batik-band" role="img" aria-label="Light blue batik-style leaf and swirl motif"></div>
    </section>
    <section class="panel front-panel">
      <div class="brand-lockup">
        <span class="brand-mark"></span>
        <span class="brand-name">LUMAVERA</span>
      </div>
      <h1 class="product-title">Amino Acid<br>Cleansing<br>Mousse</h1>
      <ul class="product-claims">
        <li>For all skin types</li>
        <li>No sulfates</li>
        <li>No synthetic colors</li>
        <li>No synthetic fragrance</li>
      </ul>
      <div class="batik-band" role="img" aria-label="Light blue batik-style leaf and swirl motif"></div>
    </section>
  </main>
</body>
</html>
```